London based Blowdry bar needs drinks menu

Volara Blowdry Bar is a successful trendy 'Blowdry bar' based in London. We offer our clients a number of services that are quick, affordable and ideal for a perfect night out!
Within the salon we offer soft & alcoholic drinks - I need to advertise this but space is limited. Therefore I would like to have a simple but pretty bar menu that will be designed like a banner and run under the mirrors at each position.
Please look at our website to have a look inside salon and pick up design ideas, colours used and feel of salon.
Website = www.quickstylelounge.co.uk
Font used for Volara logo = Houschka rounded
Font used on website = District Pro
Measurement for each menu 90cm length x 7.5cm height (horizontal menu)
Target Market(s)
20-50 year olds - clients in salon to have a fast fun experience. needs to be clear, easy to read and to the point
Font styles to use
Other font styles liked:
- District Pro
Requirements
Must have
- Title of drink, price of drink - easy to read font
Nice to have
- Nice to have a picture of drink in beginning of menu (nice visual add) to draw attention to clients eyes and so they understand it is a drinks menu. Clear points at the beginning of each drink.

```html
<!DOCTYPE html>
<html lang="en">
<head>
<meta charset="utf-8">
<title>Volara Blowdry Bar – Drinks Menu</title>
<link href="https://fonts.googleapis.com/css2?family=Nunito:wght@700;800;900&family=Arimo:wght@400;700&display=swap" rel="stylesheet">
<style>
  :root {
    --green: #7cc35a;
    --green-dark: #6db24b;
    --pink: #e3609b;
    --blush: #f4c4d7;
    --blush-light: #fae4ed;
    --ink: #1a1a1a;
    --grey: #6b6b6b;
    --white: #ffffff;
  }
  * { margin: 0; padding: 0; box-sizing: border-box; }
  html, body { width: 1200px; height: 100px; overflow: hidden; background: var(--white); }
  .banner { position: relative; width: 1200px; height: 100px; overflow: hidden; background: var(--white); font-family: "Arimo", Arial, sans-serif; color: var(--ink); }

  .drinks-visual { position: absolute; left: 0; top: 0; width: 145px; height: 100px;
    background: linear-gradient(100deg, #f3a23a 0%, #e9604a 28%, #d9ecd0 55%, #f2c6d3 78%, rgba(255,255,255,0) 100%); }

  .headline { position: absolute; left: 158px; top: 9px; width: 225px;
    font-family: "Nunito", sans-serif; font-weight: 900; font-size: 31px; line-height: 29px; color: var(--green); }

  .offers-button { position: absolute; left: 140px; top: 73px; width: 250px; height: 25px; border-radius: 4px;
    background: var(--green-dark); color: var(--white); font-weight: 700;
    font-size: 10.5px; display: flex; align-items: center; justify-content: center; }

  .watercolour-wash { position: absolute; left: 395px; top: 0; width: 660px; height: 100px;
    background:
      radial-gradient(ellipse 45% 70% at 28% 50%, var(--blush) 0%, var(--blush-light) 50%, rgba(255,255,255,0) 100%),
      radial-gradient(ellipse 40% 65% at 78% 55%, var(--blush) 0%, var(--blush-light) 50%, rgba(255,255,255,0) 100%); }

  .menu-column { position: absolute; top: 9px; list-style: none; }
  .menu-column.first { left: 430px; }
  .menu-column.second { left: 712px; }
  .menu-item { position: relative; padding-left: 14px; font-size: 17px; line-height: 21px; white-space: nowrap; }
  .menu-item::before { content: ""; position: absolute; left: 0; top: 7px; width: 7px; height: 7px; border-radius: 50%; background: var(--ink); }
  .menu-item.no-bullet::before { display: none; }
  .price { font-family: "Nunito", sans-serif; font-weight: 900; color: var(--pink); font-size: 18px; }
  .cocktail-choice { padding-left: 0; font-size: 11.5px; font-weight: 700; margin-top: 2px; }
  .cocktail-choice .price { font-size: 12px; }

  .brand { position: absolute; left: 1060px; top: 18px; width: 135px; text-align: center; }
  .brand-mark { display: flex; align-items: center; justify-content: center; gap: 7px; height: 48px; }
  .brand-dot { width: 14px; height: 14px; border-radius: 50%; background: var(--ink); }
  .brand-name { font-weight: 700; font-size: 15px; letter-spacing: 1px; color: var(--ink); }
  .brand-tagline { font-size: 9.5px; color: var(--grey); margin-top: 10px; white-space: nowrap; }
</style>
</head>
<body>
<div class="banner">
  <div class="drinks-visual" role="img" aria-label="Colourful cocktails and drinks with fruit garnish"></div>

  <h1 class="headline">Why not have<br>a drink?</h1>
  <div class="offers-button">CHECK OUT BAR BOARD FOR DRINK OFFERS</div>

  <div class="watercolour-wash" role="img" aria-label="Soft pink watercolour wash"></div>

  <ul class="menu-column first">
    <li class="menu-item">Filtered Water</li>
    <li class="menu-item">Sparkling Water <span class="price">£1.50</span></li>
    <li class="menu-item">Cola / Diet Cola <span class="price">£2</span></li>
    <li class="menu-item">100% real Fruit Juice <span class="price">£2</span></li>
  </ul>

  <ul class="menu-column second">
    <li class="menu-item">Dry White Wine / Red Wine <span class="price">£4</span></li>
    <li class="menu-item">Prosecco / Rose Prosecco <span class="price">£5</span></li>
    <li class="menu-item">&nbsp;Prosecco Cocktails :</li>
    <li class="menu-item no-bullet cocktail-choice">Choose from Elderflower, Peach, Spritz &amp; Hibiscus – <span class="price">£7</span></li>
  </ul>

  <div class="brand">
    <div class="brand-mark">
      <span class="brand-dot"></span>
      <span class="brand-name">VOLARA</span>
    </div>
    <p class="brand-tagline">beautifully blow-dried hair</p>
  </div>
</div>
</body>
</html>
```